Webpage layout and company logo combination

We are trying to renovate an existing site to make it sharper and sophisticated in appearance. This is the existing site: http://www.pellmoorrealtynj.com/agents.html . The new presentation should be bright, sharp, sophisticated and should incorporate two additional menu tabs. The menu tabs will be revised as follows: Property Listings, Property Management, Advisory & Consulting, Local Info, R/E Tools, Our Team (please disregard Korean language characters, which will be installed after English version is completed, separately).

It Company

```html
<!DOCTYPE html>
<html lang="en">
<head>
<meta charset="utf-8">
<title>Pellmoor Realty</title>
<link href="https://fonts.googleapis.com/css2?family=Open+Sans:ital,wght@0,400;0,600;0,700;1,400;1,600;1,700;1,800&family=Roboto+Condensed:wght@400;700&display=swap" rel="stylesheet">
<style>
:root{
  --olive:#b6bf8e;
  --plum:#6d2a4e;
  --plum-text:#6b2747;
  --ink:#333;
  --page:#f0f0f0;
  --page-light:#f5f5f5;
  --card:#fff;
  --band:#e6e6e6;
  --icon-grey:#9a9a9a;
}
*{box-sizing:border-box;margin:0;padding:0}
html,body{width:920px;height:1200px;overflow:hidden}
body{position:relative;background:var(--page);font-family:"Open Sans",sans-serif;color:var(--ink)}
.abs{position:absolute}

/* header */
.site-header{left:0;top:0;width:920px;height:72px;background:var(--olive)}
.brand{left:98px;top:21px;display:flex;align-items:center;gap:9px}
.brand-mark{width:28px;height:28px;background:var(--plum)}
.brand-name{font-family:"Roboto Condensed",sans-serif;font-weight:700;font-size:28px;color:#fff;line-height:30px}
.header-contact{right:97px;top:17px;text-align:right;font-style:italic;font-size:10px;line-height:19px;color:var(--plum-text);font-weight:600}

/* nav */
.main-nav{left:0;top:72px;width:920px;height:36px;background:#fff}
.nav-list{position:absolute;left:96px;top:0;display:flex;list-style:none;height:36px}
.nav-list li{height:36px;line-height:36px;text-align:center;font-family:"Roboto Condensed",sans-serif;font-size:14px;color:#333;border-right:1px solid #dcdcdc;background:linear-gradient(#fff,#e9e9e9)}
.nav-list li.active{background:var(--plum);color:#fff;font-weight:700}
.nav-list li.flag{background:#e4e4e4;border-right:0}
.nav-list li.flag svg{margin-top:8px}

/* hero */
.hero{left:0;top:108px;width:920px;height:335px;background:
  linear-gradient(180deg,rgba(255,255,255,0) 70%,rgba(0,0,0,.18) 100%),
  linear-gradient(100deg,#7a5a3e 0%,#8e6d4a 22%,#7f9a52 40%,#dcd8c8 55%,#b8b49e 64%,#7d9a4c 78%,#e2dfd2 92%,#c8c4b2 100%)}
.hero-title{left:97px;top:248px;padding:0 14px;height:38px;line-height:38px;background:rgba(40,40,40,.82);color:#fff;font-size:15.5px;font-weight:600}
.hero-text{left:97px;top:290px;width:342px;padding:5px 14px 7px;background:rgba(40,40,40,.75);color:#fff;font-size:9.5px;line-height:16.5px;font-weight:600}
.pager{left:418px;top:415px;width:84px;height:28px;background:#f0f0f0;border-radius:6px 6px 0 0;display:flex;gap:4px;justify-content:center;align-items:center}
.pager span{width:10px;height:10px;border-radius:50%;background:#999}
.pager span.on{background:#3b5c8a}

/* sections */
.section-title{font-family:"Roboto Condensed",sans-serif;font-size:16px;font-weight:400;color:var(--plum-text)}

.property{width:160px;height:212px;background:var(--card);box-shadow:0 1px 2px rgba(0,0,0,.18)}
.property-photo{position:absolute;left:0;top:0;width:160px;height:100px}
.tag-sale{position:absolute;left:0;top:0;background:#333;color:#fff;font-size:11.5px;line-height:19px;padding:0 7px}
.tag-price{position:absolute;right:0;top:80px;background:#333;color:#fff;font-style:italic;font-weight:700;font-size:11.5px;line-height:20px;padding:0 6px}
.zoom{position:absolute;left:65px;top:40px}
.property-meta{position:absolute;left:0;top:100px;width:160px;height:42px;background:var(--band);padding:4px 10px;font-size:11.5px;line-height:16px;color:#555}
.property-meta b{display:inline-block;width:48px;font-weight:400;color:var(--plum-text)}
.property-meta .city{font-size:9.5px}
.property-specs{position:absolute;left:0;top:142px;width:160px}
.property-specs div{height:22px;line-height:22px;padding:0 10px;font-size:9.5px;border-bottom:1px solid #e8e8e8;display:flex}
.property-specs b{font-weight:600;color:var(--plum-text);width:104px}

.agent{left:631px;width:194px;height:70px;background:var(--card)}
.agent-photo{position:absolute;left:10px;top:8px;width:54px;height:54px;border-radius:50%;border:2px solid #c4c4c4}
.agent-info{position:absolute;left:73px;top:10px;font-style:italic;font-size:9.5px;line-height:16.5px;color:#444}
.agent-info .name{font-size:11px;color:var(--plum-text);font-weight:600}
.agent-info .cell{color:var(--plum-text);font-weight:600}

/* cta bar */
.cta-bar{left:96px;top:942px;width:729px;height:55px;display:flex}
.cta{flex:1;display:flex;align-items:center;gap:9px;padding-left:12px;color:#fff;font-size:11px;line-height:15px;text-transform:uppercase;font-weight:600}
.cta strong{font-style:italic;font-weight:800;font-size:16px}
.cta:nth-child(1){background:#2a2a2a}
.cta:nth-child(2){background:#383838}
.cta:nth-child(3){background:#464646}
.cta:nth-child(4){background:#595959}

.lower{left:0;top:970px;width:920px;height:193px;background:var(--page-light);z-index:-1}
.dashed{border-bottom:3px dotted #ccc;padding-bottom:4px}
.news-item{left:96px;width:155px;display:flex;gap:9px;font-size:9.5px;line-height:13.5px;color:#555}
.news-thumb{width:40px;height:36px;flex:none;margin-top:1px}
.news-item i{font-weight:600;color:#333;font-size:10px}

.testimonial{left:275px;top:1019px;width:363px;height:104px;background:#fff;border:1px solid #d8d8d8}
.testimonial-tail{left:598px;top:1122px}
.testimonial-photo{position:absolute;left:6px;top:6px;width:110px;height:90px;background:linear-gradient(180deg,#c9cfd6 0%,#9aa3ad 55%,#3f3f46 100%)}
.testimonial-name{position:absolute;left:129px;top:13px;font-style:italic;font-weight:600;font-size:12px;color:var(--plum-text)}
.testimonial-text{position:absolute;left:129px;top:38px;width:226px;font-size:9.5px;line-height:17px;color:#999;text-indent:18px}
.quote{position:absolute;left:129px;top:33px;font-family:Georgia,serif;font-size:24px;line-height:24px;color:#ccc;font-weight:700}
.more{left:559px;top:1136px;font-style:italic;font-weight:600;font-size:9px}

.contact-col{left:667px;top:1016px;width:157px}
.contact-row{display:flex;gap:8px;font-size:9.5px;font-style:italic;font-weight:600;line-height:13px;margin-top:9px}
.contact-row svg{flex:none}
.social{display:flex;gap:7px;margin-top:14px}
.social span{width:22px;height:22px;border-radius:50%;border:2px solid #b4b4b4;background:#fff}
.social span:first-child{background:var(--plum);border-color:var(--plum)}

.site-footer{left:0;top:1163px;width:920px;height:37px;background:var(--olive);font-size:9.5px;line-height:37px}
.crumbs{position:absolute;left:96px;word-spacing:1px}
.crumbs a{color:#333;text-decoration:none}
.crumbs a.current{color:var(--plum-text)}
.crumbs .sep{margin:0 3px}
.copyright{position:absolute;right:97px}
</style>
</head>
<body>

<header class="site-header abs">
  <div class="brand abs"><span class="brand-mark"></span><span class="brand-name">Pellmoor Realty</span></div>
  <div class="header-contact abs">Add: 318 Alder Crest Lane , NJ 07099<br>Tel: (866)555-0142&nbsp;&nbsp;Fax: (201)555-0177</div>
</header>

<nav class="main-nav abs">
  <ul class="nav-list">
    <li class="active" style="width:53px">Home</li>
    <li style="width:113px">Property Listings</li>
    <li style="width:141px">Property Management</li>
    <li style="width:139px">Advisory &amp; Consulting</li>
    <li style="width:74px">Local Info</li>
    <li style="width:72px">R/E Tools</li>
    <li style="width:79px">Our Team</li>
    <li class="flag" style="width:58px"><svg width="32" height="20" viewBox="0 0 32 20"><rect width="32" height="20" fill="#243f8a"/><path d="M0 0L32 20M32 0L0 20" stroke="#fff" stroke-width="4"/><path d="M0 0L32 20M32 0L0 20" stroke="#c8102e" stroke-width="1.5"/><path d="M16 0V20M0 10H32" stroke="#fff" stroke-width="6"/><path d="M16 0V20M0 10H32" stroke="#c8102e" stroke-width="3.5"/></svg></li>
  </ul>
</nav>

<section class="hero abs" role="img" aria-label="Miniature model town with houses, trees and street lamps"></section>
<h1 class="hero-title abs">Welcome to Pellmoor Realty</h1>
<p class="hero-text abs">Pellmoor Realty is your online resource of buying, selling and finacing for your recidential or commercial real estate. We will assist your real estate needs uor integrity and helpful experience.</p>
<div class="pager abs"><span class="on"></span><span></span><span></span><span></span><span></span></div>

<h2 class="section-title abs" style="left:96px;top:456px">Properties</h2>

<article class="property abs" style="left:96px;top:480px">
  <div class="property-photo" role="img" aria-label="Bright townhouse living room" style="background:linear-gradient(180deg,#f4f4f2 0%,#e6e6e4 60%,#c2c0bc 100%)"></div>
  <svg class="zoom" width="24" height="24" viewBox="0 0 24 24"><circle cx="12" cy="12" r="12" fill="#3a3a3a"/><circle cx="11" cy="11" r="5" fill="none" stroke="#fff" stroke-width="1.8"/><path d="M14.6 14.6L18 18M9 11H13M11 9V13" stroke="#fff" stroke-width="1.8"/></svg>
  <span class="tag-sale">For sale</span><span class="tag-price">$625,000</span>
  <div class="property-meta"><b>Type:</b>Townhouse<br><b class="city">City:</b><span class="city">Guttenberg, NJ</span></div>
  <div class="property-specs"><div><b>Size:</b>1762</div><div><b>Bedrooms:</b>2</div><div><b>Bathrooms:</b>2</div></div>
</article>
<article class="property abs" style="left:271px;top:480px">
  <div class="property-photo" role="img" aria-label="Brick apartment complex with lawn" style="background:linear-gradient(180deg,#e4ebf2 0%,#b9a58f 45%,#5f7a44 75%,#8e8e86 100%)"></div>
  <span class="tag-sale">For sale</span><span class="tag-price">$625,000</span>
  <div class="property-meta"><b>Type:</b>Townhouse<br><b class="city">City:</b><span class="city">Guttenberg, NJ</span></div>
  <div class="property-specs"><div><b>Size:</b>1762</div><div><b>Bedrooms:</b>2</div><div><b>Bathrooms:</b>2</div></div>
</article>
<article class="property abs" style="left:446px;top:480px">
  <div class="property-photo" role="img" aria-label="Atrium with balconies and greenery" style="background:linear-gradient(120deg,#a9784a 0%,#4f6b36 40%,#9c9a8c 70%,#b07e4e 100%)"></div>
  <span class="tag-sale">For sale</span><span class="tag-price">$625,000</span>
  <div class="property-meta"><b>Type:</b>Townhouse<br><b class="city">City:</b><span class="city">Guttenberg, NJ</span></div>
  <div class="property-specs"><div><b>Size:</b>1762</div><div><b>Bedrooms:</b>2</div><div><b>Bathrooms:</b>2</div></div>
</article>
<article class="property abs" style="left:96px;top:708px">
  <div class="property-photo" role="img" aria-label="White corner building on a street" style="background:linear-gradient(180deg,#cfd9e4 0%,#eeeeea 35%,#d8d4cc 65%,#8a3a30 78%,#6e6e6e 100%)"></div>
  <span class="tag-sale">For sale</span><span class="tag-price">$625,000</span>
  <div class="property-meta"><b>Type:</b>Townhouse<br><b class="city">City:</b><span class="city">Guttenberg, NJ</span></div>
  <div class="property-specs"><div><b>Size:</b>1762</div><div><b>Bedrooms:</b>2</div><div><b>Bathrooms:</b>2</div></div>
</article>
<article class="property abs" style="left:271px;top:708px">
  <div class="property-photo" role="img" aria-label="Autumn residential street" style="background:linear-gradient(180deg,#dfe2e4 0%,#c99a6a 40%,#b8643a 58%,#8c8c8a 80%,#6d7f4a 100%)"></div>
  <span class="tag-sale">For sale</span><span class="tag-price">$625,000</span>
  <div class="property-meta"><b>Type:</b>Townhouse<br><b class="city">City:</b><span class="city">Guttenberg, NJ</span></div>
  <div class="property-specs"><div><b>Size:</b>1762</div><div><b>Bedrooms:</b>2</div><div><b>Bathrooms:</b>2</div></div>
</article>
<article class="property abs" style="left:446px;top:708px">
  <div class="property-photo" role="img" aria-label="Open kitchen and living area" style="background:linear-gradient(180deg,#ece6da 0%,#d6cab6 55%,#9a7552 100%)"></div>
  <span class="tag-sale">For sale</span><span class="tag-price">$625,000</span>
  <div class="property-meta"><b>Type:</b>Townhouse<br><b class="city">City:</b><span class="city">Guttenberg, NJ</span></div>
  <div class="property-specs"><div><b>Size:</b>1762</div><div><b>Bedrooms:</b>2</div><div><b>Bathrooms:</b>2</div></div>
</article>

<h2 class="section-title abs" style="left:631px;top:456px">Agents</h2>

<div class="agent abs" style="top:480px"><div class="agent-photo" role="img" aria-label="Portrait of agent Martin Cole" style="background:linear-gradient(180deg,#e6e2de,#7a3a3a)"></div><div class="agent-info"><div class="name">Martin Cole</div><div class="cell">Cell: 201-555-0131</div>mcole22@pellmoor.com</div></div>
<div class="agent abs" style="top:553px"><div class="agent-photo" role="img" aria-label="Portrait of agent Dana Reyes" style="background:linear-gradient(180deg,#7fa85a,#ead8c8)"></div><div class="agent-info"><div class="name">Dana Reyes</div><div class="cell">Cell: (917)555-0164</div>dreyes22@pellmoor.com</div></div>
<div class="agent abs" style="top:627px"><div class="agent-photo" role="img" aria-label="Portrait of agent Lena Park" style="background:linear-gradient(180deg,#2f63a3,#dcbca0)"></div><div class="agent-info"><div class="name">Lena Park</div><div class="cell">Cell: (201)555-0119</div>lpark22@pellmoor.com</div></div>
<div class="agent abs" style="top:700px"><div class="agent-photo" role="img" aria-label="Portrait of agent Owen Hart" style="background:linear-gradient(180deg,#9cc4e0,#2c3440)"></div><div class="agent-info"><div class="name">Owen Hart</div><div class="cell">Cell: (201)555-0186</div>ohart22@pellmoor.com</div></div>
<div class="agent abs" style="top:774px"><div class="agent-photo" role="img" aria-label="Portrait of agent Ryan Ito" style="background:linear-gradient(180deg,#f2e2a0,#2e2e2e)"></div><div class="agent-info"><div class="name">Ryan Ito</div><div class="cell">Cell: (201)555-0108</div>rito22@pellmoor.com</div></div>
<div class="agent abs" style="top:847px"><div class="agent-photo" role="img" aria-label="Portrait of agent Grace Min Soo" style="background:linear-gradient(180deg,#f6ece2,#c88a6c)"></div><div class="agent-info"><div class="name">Grace Min Soo</div><div class="cell">Cell: (201)555-0153</div>rito22@pellmoor.com</div></div>

<div class="lower abs"></div>

<div class="cta-bar abs">
  <div class="cta"><svg width="22" height="26" viewBox="0 0 22 26"><path d="M10 2L19 6 17 21 8 24 3 14Z" fill="#fff" transform="rotate(-20 11 13)"/><circle cx="12" cy="8" r="2" fill="#2a2a2a"/><path d="M9 13H14M9 16H13" stroke="#2a2a2a" stroke-width="1.5"/></svg><span>Click here for <strong>Free</strong><br>Appraisal</span></div>
  <div class="cta"><svg width="26" height="22" viewBox="0 0 26 22"><path d="M2 7Q13 0 24 7L21 10 17 8V6Q13 4 9 6V8L5 10Z" fill="#fff"/><rect x="5" y="11" width="16" height="9" rx="2" fill="none" stroke="#fff" stroke-width="2"/><circle cx="13" cy="15.5" r="2" fill="#fff"/></svg><span>Call us<br><strong>(866)555-0142</strong></span></div>
  <div class="cta"><svg width="22" height="26" viewBox="0 0 22 26"><rect x="2" y="2" width="18" height="22" rx="2" fill="#fff"/><path d="M6 9H16M6 13H16M6 17H16" stroke="#464646" stroke-width="2"/></svg><span>Online <strong>Property</strong><br>Magazine</span></div>
  <div class="cta"><svg width="34" height="26" viewBox="0 0 34 26"><rect x="2" y="2" width="18" height="22" fill="none" stroke="#fff" stroke-width="2"/><rect x="5" y="5" width="12" height="5" fill="#fff"/><path d="M6 14H9M13 14H16M6 19H9M13 19H16" stroke="#fff" stroke-width="2"/><path d="M29 5V23M32 9Q32 7 28.5 7Q25 7 25 10Q25 13 28.5 14Q32 15 32 18Q32 21 28.5 21Q25 21 25 19" stroke="#fff" stroke-width="2" fill="none"/></svg><span>Loan online<br><strong>Calculator</strong></span></div>
</div>

<h2 class="section-title abs dashed" style="left:96px;top:1014px;width:155px">News</h2>
<div class="news-item abs" style="top:1050px"><div class="news-thumb" role="img" aria-label="News photo of a conference guest" style="background:linear-gradient(180deg,#e9b05a,#c2562e)"></div><div><i>Monday 03 Mar 2014</i><br>Conference Overview<br>We hope to see the....</div></div>
<div class="abs" style="left:96px;top:1098px;width:155px;border-top:1px solid #ddd"></div>
<div class="news-item abs" style="top:1107px"><div class="news-thumb" role="img" aria-label="News photo of a conference guest" style="background:linear-gradient(180deg,#7a2e2e,#e2c0a4)"></div><div><i>Monday 03 Mar 2014</i><br>Conference Overview<br>We hope to see the....</div></div>

<div class="testimonial abs">
  <div class="testimonial-photo" role="img" aria-label="Portrait of a satisfied client"></div>
  <div class="testimonial-name">Client Name</div>
  <span class="quote">&ldquo;</span>
  <p class="testimonial-text">Lorem ipsum dolor sit amet, ctetur adipiscing elit. Nullam volutpat egestas neque, non hendrerit ipsum fringilla quis. Donec ut neque mauris.</p>
</div>
<svg class="testimonial-tail abs" width="14" height="10" viewBox="0 0 14 10"><path d="M0 0L7 9 14 0" fill="#fff" stroke="#d8d8d8"/><path d="M1 0H13" stroke="#fff" stroke-width="2"/></svg>
<div class="more abs">More Testimonials</div>

<div class="contact-col abs">
  <h2 class="section-title dashed">Pellmoor Realty</h2>
  <div class="contact-row"><svg width="16" height="16" viewBox="0 0 16 16"><path d="M8 1C5 1 3.5 3 3.5 5.5C3.5 9 8 13 8 13S12.5 9 12.5 5.5C12.5 3 11 1 8 1Z" fill="none" stroke="#6b2747" stroke-width="1.5"/><circle cx="8" cy="5.5" r="1.6" fill="#6b2747"/><path d="M2 15H14" stroke="#6b2747" stroke-width="1.5"/></svg><span>318 Alder Crest Lane , NJ 07099</span></div>
  <div class="contact-row"><svg width="16" height="14" viewBox="0 0 14 14"><path d="M3 1L5 1 6 4 4.5 5.5Q6 8.5 8.5 9.5L10 8 13 9V11Q12 13 10 13Q2 11 1 3Q1 1 3 1Z" fill="#6b2747"/></svg><span>(866)555-0142</span></div>
  <div class="contact-row"><svg width="16" height="14" viewBox="0 0 14 14"><rect x="1" y="3" width="12" height="8" fill="#6b2747"/><path d="M1 3L7 8 13 3" stroke="#fff" fill="none"/></svg><span>mcole22@pellmoor.com</span></div>
  <div class="social" aria-label="Social links"><span></span><span></span><span></span><span></span><span></span></div>
</div>

<footer class="site-footer abs">
  <div class="crumbs"><a class="current" href="#">Home</a><span class="sep">/</span><a href="#">Property Listings</a><span class="sep">/</span><a href="#">Property Management</a><span class="sep">/</span><a href="#">Advisory &amp; Consulting</a><span class="sep">/</span><a href="#">Local Info</a><span class="sep">/</span><a href="#">R/E Tools</a><span class="sep">/</span><a href="#">Our Team</a></div>
  <div class="copyright">Pellmoor Realty © 2014. All Rights Reserved.</div>
</footer>

</body>
</html>
```